Marlow Estate Services (Handyman / Home Improvement Company)

Looking for a double sided professional looking business card with Logo attached to be highlighted on one side and throwing in an image of a handyman as an option would be nice to see as well. We are a company focused on providing quality Handyman and Home improvement services in a timely manner that is done right the first time with integrity

Industry/Entity Type

Handyman / Home Improvement

Contact Information for Business Card

(LOGO, Name, Mobile and office phone numbers, email) on front side of card, (the words "The SOLUTION to all of your Handyman and Home Improvement needs" followed by "Family Owned and Operated" at the very bottom) on the back.

Colors
EB3D1F
EC4F4E
F09395
F8D3D4
FCEDEE

Requirements
Must have
• Red, Gray, Black Color scheme
Should not have
• No Yellow or Blue colors

```html
<!DOCTYPE html>
<html lang="en">
<head>
<meta charset="utf-8">
<title>Marlow Estate Services – Business Card</title>
<link href="https://fonts.googleapis.com/css2?family=Montserrat:wght@400;700;800&family=Oswald:wght@700&display=swap" rel="stylesheet">
<style>
  :root {
    --red: #eb3d1f;
    --card-red: #e92d2f;
    --ink: #1f1f1f;
    --gray: #3a3a3a;
    --white: #ffffff;
    --stage: #1c1c1c;
    --pink-soft: #f09395;
  }
  * { margin: 0; padding: 0; box-sizing: border-box; }
  html, body { width: 1200px; height: 1059px; overflow: hidden; }
  body { background: var(--stage); font-family: "Montserrat", sans-serif; position: relative; }

  .card { position: absolute; left: 262px; width: 716px; height: 409px; border-radius: 26px; overflow: hidden; }

  /* Front */
  .card-front { top: 95px; background: var(--white); }
  .brand-front {
    position: absolute; left: 417px; top: 60px; width: 265px;
    text-align: center; color: var(--red);
    font-family: "Montserrat", sans-serif; font-weight: 800; font-size: 34px; line-height: 1.1;
    text-transform: uppercase;
  }
  .person-name { position: absolute; left: 35px; top: 248px; font-size: 28px; font-weight: 700; color: var(--red); }
  .person-role { position: absolute; left: 35px; top: 290px; font-size: 19px; font-weight: 400; color: var(--ink); }
  .divider { position: absolute; left: 35px; top: 329px; width: 648px; height: 2px; background: var(--gray); }
  .contact-row { position: absolute; left: 35px; top: 346px; width: 660px; display: flex; align-items: center; gap: 18px; font-size: 18.5px; color: var(--ink); white-space: nowrap; }
  .contact-item { display: flex; align-items: center; gap: 10px; }
  .contact-item svg { flex: none; }
  .footer-band { position: absolute; left: 0; bottom: 0; width: 100%; height: 12px; }

  /* Back */
  .card-back { top: 529px; background: var(--card-red); }
  .handyman-art {
    position: absolute; left: 8px; top: 62px; width: 330px; height: 347px;
    background: linear-gradient(180deg, #f2a98a 0%, #4a5a72 60%, #d9a441 100%);
    opacity: 0.35; border-radius: 12px 12px 0 0;
  }
  .tagline { position: absolute; left: 300px; width: 406px; text-align: center; color: var(--white); }
  .tagline-lead { top: 16px; font-size: 21px; font-weight: 700; }
  .tagline-main { font-family: "Oswald", sans-serif; font-weight: 700; font-size: 35px; line-height: 1; transform: scaleX(0.9); }
  .tagline-main.line-one { top: 50px; }
  .tagline-main.line-two { top: 95px; }
  .brand-back {
    position: absolute; left: 366px; top: 180px; width: 276px;
    text-align: center; color: var(--white);
    font-weight: 800; font-size: 36px; line-height: 1.1; text-transform: uppercase;
  }
  .family-note { position: absolute; left: 300px; width: 406px; top: 360px; text-align: center; color: var(--white); font-size: 21px; font-weight: 700; }
</style>
</head>
<body>

  <section class="card card-front">
    <div class="brand-front">Marlow<br>Estate<br>Services</div>

    <h1 class="person-name">Daniel Hartley</h1>
    <p class="person-role">Owner</p>
    <div class="divider"></div>

    <div class="contact-row">
      <span class="contact-item">
        <svg width="14" height="22" viewBox="0 0 14 22"><rect x="1.5" y="1.5" width="11" height="19" rx="2" fill="none" stroke="var(--red)" stroke-width="2"/><circle cx="7" cy="17" r="1.4" fill="var(--red)"/></svg>
        044-555 210 347
      </span>
      <span class="contact-item">
        <svg width="20" height="16" viewBox="0 0 20 16"><path d="M1 6 Q10 -1 19 6 L16 8 L14 5 Q10 4 6 5 L4 8 Z" fill="var(--red)"/><rect x="4" y="8" width="12" height="7" rx="1.5" fill="var(--red)"/></svg>
        044-555 210 347
      </span>
      <span class="contact-item">
        <svg width="20" height="14" viewBox="0 0 20 14"><rect x="0" y="0" width="20" height="14" rx="1" fill="var(--red)"/><path d="M1 1 L10 8 L19 1" fill="none" stroke="var(--white)" stroke-width="2"/></svg>
        hello@marlowestate.com
      </span>
    </div>

    <svg class="footer-band" viewBox="0 0 716 12" preserveAspectRatio="none">
      <polygon points="0,0 352,0 358,12 0,12" fill="var(--card-red)"/>
      <polygon points="358,0 716,0 716,12 364,12" fill="var(--gray)"/>
    </svg>
  </section>

  <section class="card card-back">
    <div class="handyman-art" role="img" aria-label="Illustration of a smiling handyman in overalls holding a pipe wrench with a tool belt"></div>

    <p class="tagline tagline-lead">Your SOLUTION to all of</p>
    <p class="tagline tagline-main line-one">your Handyman and</p>
    <p class="tagline tagline-main line-two">Home Improvement Needs</p>

    <div class="brand-back">Marlow<br>Estate<br>Services</div>

    <p class="family-note">Family Owned and Operated</p>
  </section>

</body>
</html>
```